San Francisco Leading Consulting firm - Quorvane Web Design Project

•Create a Web Design
•Uncoded webpage layout design
•2 Pages Design - Homepage + Interior Page

Task Description
Hello, we're looking for a re-design our current website www.quorvane-example.com

we have a sample mockup design @

http://quorvane.pubmirrex-example.org/

This shows the layout that we like and also a sample of 6 pictures that would change based on where you mouse over..

6 pictures HOME design needs to be included.

SMART
THOUGHTFUL
FLEXIBLE
CREATIVE SERVICES
TECHNICAL SERVICES
PARTNERS

sites we like:

http://www.belvantoadvisory-example.com/Home.cfm?id=Home
http://www.plumstudioworks-example.com/index.html

Our company can be best described as: 100+ employees, cutting-edge, depandable, innovative, strong, smart.

Our Primary focus is: IT Consulting Services and Creative Design services

Quorvane LLC is a consulting firm providing creative design, business and technology solutions to both private and public interests.

Established in 1996, Quorvane is a San Francisco based company providing specialists for a range of business needs including:

Creative Design Services
•Print
•Logo Design
•Website Design
•Illustration

and

Business and Technology solutions

•Application Software and Web Development
•Business Process Re-Design (BPR)
•Business/Systems Analysis and Requirement Documentation
•Mentoring and Training
•Network/Hardware Installation Services
•System Design and Architecture
•Vendor Management
•Sharepoint Architecture and Implementation

our sample mockup site:

Reason: Due to holiday season, we're not available to work with designers and finilize our design.  

Thank you very much for submitting your design.

We appreciate your time and creativity.   Since, our office is currently closed for holidays, we will be reviewing it in details next week and will make our decision as soon as possible.

It would be great if you could submit any of your changes by Wed next week, so it would be part of our reviews. 

Please see updated wireframe under attachments:  we have some minor updates to our wireframe that we would like you to update your designs, if possible.  

We also encorouge you not to use our standard wireframe and come up with more unique designs.   Everything would be considered when we review your design.

 

Target Market(s)

Creative services and professional services clients, including government agencies

Industry/Entity Type

Business

Requirements
Must have
• Clean, professional look, easy navigation

```html
<!DOCTYPE html>
<html lang="en">
<head>
<meta charset="utf-8">
<title>Quorvane — Home</title>
<link rel="stylesheet" href="https://fonts.googleapis.com/css2?family=PT+Sans+Narrow:wght@400;700&family=Open+Sans:wght@400;600;700&display=swap">
<style>
  :root {
    --ink: #2b2b2b;
    --dark: #3a3a3a;
    --darker: #2a2a2a;
    --bar: #333333;
    --blue: #2a8fd0;
    --blue-deep: #1f78b4;
    --text: #333333;
    --frame: #f4f4f4;
    --page-top: #d9d9d9;
    --page-mid: #ececec;
    --footer: #4a4a4a;
    --gold: #e8b21c;
  }
  * { box-sizing: border-box; margin: 0; padding: 0; }
  html, body { width: 1200px; height: 900px; overflow: hidden; }
  body {
    position: relative;
    font-family: "Open Sans", Arial, sans-serif;
    color: var(--text);
    background:
      radial-gradient(ellipse 700px 320px at 820px 260px, rgba(255,255,255,.75), rgba(255,255,255,0) 70%),
      radial-gradient(ellipse 500px 260px at 150px 300px, rgba(255,255,255,.55), rgba(255,255,255,0) 70%),
      linear-gradient(180deg, var(--page-top) 0px, #c9c9c9 240px, var(--page-mid) 500px, #f1f1f1 900px);
  }

  /* Header */
  .brand {
    position: absolute; left: 136px; top: 36px;
    display: flex; align-items: center; gap: 14px;
  }
  .brand-dot { width: 56px; height: 56px; border-radius: 50%; background: var(--blue); }
  .brand-name {
    font-family: "Open Sans", Arial, sans-serif; font-weight: 400;
    font-size: 44px; color: #4a4a4a; letter-spacing: 1px;
  }

  .main-nav {
    position: absolute; left: 434px; top: 0; width: 626px; height: 48px;
    background: var(--bar);
    display: flex; align-items: stretch;
  }
  .main-nav a {
    font-family: "PT Sans Narrow", Arial, sans-serif; font-weight: 700;
    font-size: 17px; color: #fff; text-decoration: none; text-transform: uppercase;
    white-space: nowrap; line-height: 34px; height: 48px; position: relative;
    text-align: center;
  }
  .nav-company { width: 90px; }
  .nav-technical { width: 180px; }
  .nav-creative { width: 156px; }
  .nav-partners { width: 94px; }
  .nav-contact { width: 106px; }
  .main-nav a.is-active { background: var(--darker); }
  .main-nav a.is-active::after {
    content: ""; position: absolute; left: 50%; top: 36px; margin-left: -6px;
    border-left: 6px solid transparent; border-right: 6px solid transparent;
    border-top: 6px solid #fff;
  }

  .dropdown {
    position: absolute; z-index: 5; left: 434px; top: 60px; width: 226px;
    background: var(--dark); padding: 8px 0 10px; list-style: none;
  }
  .dropdown li {
    font-size: 15px; color: #fff; height: 26px; line-height: 26px;
    padding-left: 30px; position: relative; white-space: nowrap;
  }
  .dropdown li::before {
    content: ""; position: absolute; left: 14px; top: 9px;
    border-top: 4px solid transparent; border-bottom: 4px solid transparent;
    border-left: 6px solid #fff;
  }
  .dropdown li.is-current { background: var(--darker); }

  .login {
    position: absolute; left: 978px; top: 62px;
    display: flex; align-items: center; gap: 6px;
    font-size: 15px; color: var(--ink);
  }

  /* Feature slider */
  .feature {
    position: absolute; left: 104px; top: 126px; width: 990px; height: 364px;
    background: var(--frame); border: 1px solid #dcdcdc;
    box-shadow: 0 2px 6px rgba(0,0,0,.12);
  }
  .tab {
    position: absolute; top: 14px; height: 334px;
    background: var(--dark); color: #fff;
  }
  .tab-num {
    position: absolute; top: 12px; left: 0; width: 100%; text-align: center;
    font-family: "Open Sans", Arial, sans-serif; font-size: 22px; color: #fff;
  }
  .tab-label {
    position: absolute; bottom: 14px; left: 50%;
    writing-mode: vertical-rl; transform: translateX(-50%) rotate(180deg);
    font-size: 28px; color: var(--blue); white-space: nowrap; line-height: 1;
  }
  .tab-current { left: 14px; width: 52px; background: var(--blue); }
  .tab-current .tab-num { color: #fff; left: 8px; text-align: left; }
  .tab-current .tab-label { color: #fff; }
  .tab-current::after {
    content: ""; position: absolute; right: -14px; top: 14px;
    border-top: 14px solid transparent; border-bottom: 14px solid transparent;
    border-left: 14px solid var(--blue);
  }

  .slide {
    position: absolute; left: 66px; top: 14px; width: 690px; height: 334px;
    background: radial-gradient(ellipse at 70% 35%, #4a4d4f, #1f2123 70%);
  }
  .slide-copy {
    position: absolute; left: 36px; top: 108px; color: #fff;
    font-family: "Open Sans", Arial, sans-serif; font-weight: 600;
  }
  .slide-copy .l1 { font-size: 38px; line-height: 44px; }
  .slide-copy .l2 { font-size: 28px; line-height: 34px; }
  .slide-copy .l3 { font-size: 28px; line-height: 36px; padding-left: 92px; }

  .tab-2 { left: 760px; width: 48px; }
  .tab-3 { left: 814px; width: 48px; }
  .tab-4 { left: 866px; width: 48px; }
  .tab-5 { left: 918px; width: 48px; }

  /* Audience columns */
  .audience { position: absolute; top: 532px; width: 312px; }
  .audience-1 { left: 120px; }
  .audience-2 { left: 438px; }
  .audience-3 { left: 758px; }
  .audience-bar {
    height: 36px; background: var(--bar); display: flex; align-items: center;
    padding-left: 10px; gap: 8px;
    font-family: "Open Sans", Arial, sans-serif; font-weight: 700;
    font-size: 19px; color: var(--blue);
  }
  .audience-bar::before {
    content: ""; width: 12px; height: 12px; border-radius: 50%; background: var(--blue);
  }
  .audience h2 {
    margin-top: 22px; font-size: 22px; font-weight: 700; color: var(--blue-deep);
    line-height: 28px;
  }
  .audience-photo { margin-top: 10px; width: 312px; height: 90px; }
  .audience-1 .audience-photo { background: linear-gradient(120deg, #e27a1f, #f2a85a 45%, #c9a07a 75%, #8c6a5a); }
  .audience-2 .audience-photo { background: linear-gradient(120deg, #c9ccd1, #8d9299 50%, #dfe2e6); }
  .audience-3 .audience-photo { background: linear-gradient(120deg, #d7dadd, #b7bcc2 50%, #5c5a5c 75%, #e3e5e7); }
  .audience p {
    margin-top: 10px; font-size: 15px; line-height: 19px; color: var(--text); height: 92px;
  }
  .learn-more {
    position: absolute; top: 312px; left: 0;
    font-size: 15px; color: var(--blue-deep); text-decoration: underline;
  }

  .site-footer {
    position: absolute; left: 0; bottom: 0; width: 1200px; height: 26px;
    background: var(--footer); color: #d6d6d6; font-size: 12px;
    text-align: center; line-height: 26px;
  }
</style>
</head>
<body>
  <header>
    <div class="brand">
      <span class="brand-dot"></span>
      <span class="brand-name">Quorvane</span>
    </div>

    <nav class="main-nav">
      <a class="nav-company is-active" href="#">Company</a>
      <a class="nav-technical" href="#">Technical Services</a>
      <a class="nav-creative" href="#">Creative Services</a>
      <a class="nav-partners" href="#">Partners</a>
      <a class="nav-contact" href="#">Contact Us</a>
    </nav>

    <ul class="dropdown">
      <li>About Quorvane</li>
      <li class="is-current">Management Team</li>
      <li>Technical Experience</li>
      <li>Our Approach</li>
      <li>News and Events</li>
      <li>Careers</li>
    </ul>

    <div class="login">
      <span>Login</span>
      <svg width="16" height="18" viewBox="0 0 16 18" aria-hidden="true">
        <path d="M4 8V5a4 4 0 0 1 8 0v3" fill="none" stroke="var(--gold)" stroke-width="2"/>
        <rect x="1" y="8" width="14" height="10" rx="1" fill="var(--gold)"/>
      </svg>
    </div>
  </header>

  <section class="feature">
    <div class="tab tab-current">
      <span class="tab-num">01.</span>
      <span class="tab-label">smart</span>
    </div>
    <div class="slide" role="img" aria-label="Hand writing equations in chalk on a blackboard">
      <div class="slide-copy">
        <div class="l1">We don’t believe</div>
        <div class="l2">in the term</div>
        <div class="l3">-“overqualified”</div>
      </div>
    </div>
    <div class="tab tab-2"><span class="tab-num">02.</span><span class="tab-label">flexible</span></div>
    <div class="tab tab-3"><span class="tab-num">03.</span><span class="tab-label">creative services</span></div>
    <div class="tab tab-4"><span class="tab-num">04.</span><span class="tab-label">technical services</span></div>
    <div class="tab tab-5"><span class="tab-num">05.</span><span class="tab-label">partners</span></div>
  </section>

  <main>
    <article class="audience audience-1">
      <div class="audience-bar">for graphic designers</div>
      <h2>Get Creative!</h2>
      <div class="audience-photo" role="img" aria-label="Orange paint and a brush on a textured canvas"></div>
      <p>Quorvane is looking for top creative talent to deliver graphic design solutions for some leading global brands Do you have what it takes?</p>
      <a class="learn-more" href="#">Learn More</a>
    </article>

    <article class="audience audience-2">
      <div class="audience-bar">for clients</div>
      <h2>The Quorvane Difference</h2>
      <div class="audience-photo" role="img" aria-label="Business colleagues meeting in an office"></div>
      <p>Smart, Flexible, Thoughtful: find out why leading corporations and government agencies are turning to Quorvane to help manage their most demanding IT services challenges.</p>
      <a class="learn-more" href="#">Learn More</a>
    </article>

    <article class="audience audience-3">
      <div class="audience-bar">for partners</div>
      <h2>Team Up With the Best</h2>
      <div class="audience-photo" role="img" aria-label="Smiling businesswoman with colleagues"></div>
      <p>When it comes to technology partnerships, our mission it so make you a success.</p>
      <a class="learn-more" href="#">Learn More</a>
    </article>
  </main>

  <footer class="site-footer">Copyright 2010, Quorvane, LLC All rights reserved.</footer>
</body>
</html>
```